Dentistry Office

We want a new design for a Dentist's office website.

The theme is: "We provide high quality, state-of-the-art, dental care in a comfortable, caring environment."

The site currently has a menu on the left of the page with about 40 items on it. There is a great deal of textual content on each page, plus several illustrations.

We want to do this using CSS, so we need specifications in the CSS for all possible elements. The CSS needs to be named in a logical manner for easy use.

Every dentist on the planet seems to use lots of Flash. We don't want to because it is so distracting. We are looking for an elegant solution targeting 24-55 age group, but not excluding anyone.

The following (from another dentist's site) can give you a taste of what we want to communicate on the site:

"After 20 years of teaching dentists how to refine their technique and many years of writing textbooks, I currently devote my time to my office and the hands-on practice of dentistry. I'd like to welcome you personally to my dental practice, and I invite you to meet my highly experienced team of professionals.

"We have offered complete dental care of the highest quality since 1978. We provide Preventive Services, Tooth Whitening and Cosmetic Dentistry for a beautiful smile, Endodontics (root canal treatment) to treat painful teeth, Sedation Dentistry so you can relax, and Dental Implants to restore what is missing. We offer total care.

"Our approach to your health is simple: We use our education, experience and dedication to provide every patient with superior dental care.

"This passion for excellence is not just a goal, but a standard every member of our team holds.

"We also pride ourselves with our state of the art procedures, training and technology. This includes creating a beautiful smile using techniques that preserve as much of the original tooth as possible.

"Our abilities are renowned throughout the dental profession and I hope if you have any questions you will contact us by an e-mail note, by phone or just by dropping by."

Keep in mind the screen shape and dimensions. Your design needs to work in the normal screen proportions, regardless of how it looks when you post it here. Scrolling is OK, but the first impression needs to work.

Keep in mind that there will be about 250 words, or more, on each page.

Competitors web sites:

http://www.brevalkoortho.example/

http://www.quimbelfieldcare.example/

http://www.grinsatdoverellclinic.example/

http://www.trunwickfamilydentalcare.example/

http://www.morvanhaledental.example/

http://www.ubrigandental.example/

We need to compete with these.

Target Market(s)

Generally adults seeking the most experienced and comfortable-to-be-with dentist.

Industry/Entity Type

Training

Requirements
Must have
• Must stand apart from other dentists.
• Must be elegant.
• Must have a horizontal menu structure across all columns, NOT a vertical that requires scrolling, no popout, pop down, etc. menus.
• We are looking for something special.
• Do not waste your time or ours putting up templates and things you have used before.
• Personally, I do not see how someone outside the US can understand the northern California dental market. But you are welcome to try.
Should not have
• Flash or graphics that move
• The look of a template
• Folksy fonts
• Looks like you used it 20 times before

```html
<!DOCTYPE html>
<html lang="en">
<head>
<meta charset="utf-8">
<title>Nolan Pravett, DDS — Santa Rosa Dentist</title>
<link rel="stylesheet" href="https://fonts.googleapis.com/css2?family=Arimo:wght@400;700&family=Roboto+Condensed:wght@400;700&family=Gelasio&display=swap">
<style>
:root{
  --orange:#d2642d;
  --orange-dark:#b9501f;
  --slate:#454e56;
  --slate-side:#6f8088;
  --ink:#333a40;
  --text:#555;
  --olive:#6f7a25;
  --panel:#f0f2f3;
  --rule:#dfe2e4;
  --menu:#dde1e4;
}
*{margin:0;padding:0;box-sizing:border-box}
html,body{width:1200px;height:1167px;overflow:hidden}
body{background:linear-gradient(#6e7f87,#c3c8ca);font-family:Arimo,Arial,sans-serif;color:var(--text);position:relative}
.page{position:absolute;left:118px;top:0;width:950px;height:1167px;background:#fff}
.abs{position:absolute}
.header{left:0;top:0;width:950px;height:130px;background:linear-gradient(#e8eaeb,#fff 80%)}
.brand{left:35px;top:30px;font-family:"Roboto Condensed",sans-serif;font-weight:700;font-size:34px;color:var(--ink);letter-spacing:-.5px}
.tagline{left:130px;top:70px;font-size:17px;color:var(--orange)}
.appt{left:700px;top:25px;font-family:"Roboto Condensed",sans-serif;font-weight:700;font-size:18px;color:var(--orange)}
.appt-phone{left:735px;top:54px;font-weight:700;font-size:18px;color:var(--ink)}
.appt-icon{left:666px;top:22px}
.nav{left:0;top:130px;width:950px;height:38px;background:linear-gradient(#dd7443,var(--orange-dark));display:flex;border-top:1px solid #e58a5d}
.nav a{color:#fff;text-decoration:none;font-size:15px;line-height:37px;padding:0 20px;border-right:1px solid #e89a72;white-space:nowrap}
.nav a:first-child{width:133px;text-align:center;padding-left:42px}
.nav a:last-child{border:none}
.side-menu{left:0;top:168px;width:238px}
.side-menu a{display:block;height:33.6px;line-height:33px;padding-left:38px;font-size:14px;color:#333;background:linear-gradient(#e4e8ea,#d7dcdf);border-bottom:1px solid #fff;text-decoration:none;position:relative}
.side-menu a::before{content:"»";position:absolute;left:16px;color:#666}
.side-menu a.active{background:var(--slate-side);color:#fff}
.side-menu a.active::before{color:#fff}
.banner{left:240px;top:168px;width:710px;height:166px;background:linear-gradient(90deg,#b9a48c,#d9c5b1 45%,#e8efeb 60%,#dcebe3)}
.banner-title{left:672px;top:210px;font-family:Gelasio,Georgia,serif;font-size:34px;line-height:38px;color:var(--ink)}
.testimonials{left:6px;top:338px;width:230px;height:453px;background:var(--panel);border:1px solid var(--rule)}
.testimonials h3{position:absolute;left:67px;top:18px;font-family:"Roboto Condensed",sans-serif;font-size:21px;color:var(--ink)}
.quote-mark{position:absolute;font-family:Gelasio,serif;font-size:40px;color:#c9ced2;line-height:1}
.testimonials p{position:absolute;left:28px;top:91px;width:180px;font-size:11.5px;line-height:17px;color:#333}
.portrait{position:absolute;left:0;top:273px;width:228px;height:178px;background:linear-gradient(#e6ece4,#c8c59b 60%,#a9a36a)}
.special{left:8px;top:803px;width:228px;height:186px;border:1px solid #cfd3d6;background:linear-gradient(#fff,#dfe2e5)}
.special-photo{position:absolute;left:0;top:0;width:110px;height:74px;background:linear-gradient(90deg,#c7b0a0,#ece9e6)}
.special h4{position:absolute;left:92px;top:18px;width:130px;text-align:right;font-family:"Roboto Condensed",sans-serif;font-size:20px;line-height:22px;color:var(--orange-dark)}
.special p{position:absolute;left:0;top:86px;width:226px;text-align:center;font-weight:700;font-size:14.5px;line-height:20px;color:var(--ink)}
.special small{position:absolute;left:0;bottom:0;width:226px;height:36px;background:#fff;border-top:1px solid #d8dcdf;padding:5px 0 0 22px;font-size:10.5px;line-height:15px;color:#333}
.section-title{font-family:"Roboto Condensed",sans-serif;font-weight:700;font-size:21px;color:var(--orange);border-bottom:3px solid #e9ebec;padding-bottom:2px}
.welcome{left:250px;top:355px;width:680px;padding-left:5px}
.providers{left:250px;top:679px;width:698px}
.lead{left:250px;top:396px;width:620px;text-align:center;font-family:"Roboto Condensed",sans-serif;font-weight:700;font-size:16px;line-height:24px;color:var(--ink)}
.intro{left:259px;top:466px;width:420px;font-size:12.5px;line-height:17px;color:#555}
.intro p{margin-bottom:17px}
.intro b{color:#333}
.motto{left:259px;top:599px;width:420px;text-align:center;font-family:"Roboto Condensed",sans-serif;font-weight:700;font-size:16.5px;line-height:24px;color:var(--olive)}
.office-photo{left:707px;top:463px;width:222px;height:166px;border:1px solid #ccc;padding:3px;background:#fff}
.office-photo div{width:100%;height:100%;background:linear-gradient(#6c7880,#7c8a6a 55%,#b6bcc3)}
.services{left:262px;top:722px;width:680px;list-style:none;font-size:12.5px;color:#555}
.services li{position:relative;padding-left:22px;line-height:26px}
.services li svg{position:absolute;left:0;top:8px}
.services b{color:var(--ink);font-size:13px}
.footer{left:0;top:1022px;width:950px;height:145px;background:var(--slate);color:#c7ccd0;font-size:12px}
.footer h3{position:absolute;left:21px;top:11px;font-family:"Roboto Condensed",sans-serif;font-size:19px;color:#fff}
.footer .name{position:absolute;left:21px;top:38px;color:#fff;font-weight:700;font-size:13px}
.footer .info{position:absolute;left:21px;top:59px;width:300px;line-height:18px}
.footer .info b{color:#fff}
.footer .addr{position:absolute;left:21px;top:100px;line-height:18px}
.footer-links{position:absolute;left:358px;top:38px;width:520px;text-align:center;font-size:13px;line-height:26px}
.footer-links span{margin:0 13px}
.copyright{position:absolute;left:425px;top:112px;font-size:12px}
</style>
</head>
<body>
<div class="page">
  <header class="abs header"></header>
  <div class="abs brand">Nolan Pravett, DDS</div>
  <div class="abs tagline">Santa Rosa Dentist</div>
  <svg class="abs appt-icon" width="28" height="28" viewBox="0 0 28 28"><circle cx="14" cy="14" r="12" fill="none" stroke="#ccc" stroke-width="2"/><path d="M10 7c-2 2-2 12 3 14l2-3-2-2c-1-2-1-3 0-5l2-1-1-4z" fill="var(--orange)"/></svg>
  <div class="abs appt">For Appointment call at:</div>
  <div class="abs appt-phone">(707) 555-0142.</div>

  <nav class="abs nav">
    <a href="#">Home</a><a href="#">Why we are different</a><a href="#">Technologies we offer</a><a href="#">Meet Dr. Pravett</a><a href="#">Our Staff</a><a href="#">Contact Us</a>
  </nav>

  <div class="abs side-menu">
    <a class="active" href="#">Education</a><a href="#">Preventative</a><a href="#">Cosmetics</a><a href="#">Restorations</a><a href="#">Visiting our office</a>
  </div>

  <div class="abs banner" role="img" aria-label="Smiling family of four: two children and their parents"></div>
  <div class="abs banner-title">Dentist for<br>Beautiful Smiles</div>

  <aside class="abs testimonials">
    <svg style="position:absolute;left:18px;top:16px" width="30" height="30" viewBox="0 0 30 30"><rect x="6" y="2" width="20" height="16" fill="#ccc"/><rect x="2" y="8" width="20" height="16" fill="#c0302a"/><circle cx="12" cy="15" r="3" fill="#fff"/></svg>
    <h3>Tesimonials</h3>
    <span class="quote-mark" style="left:12px;top:62px">“</span>
    <p>Lorem Ipsum is simply dummy text of the printing and typesetting industry. Lorem Ipsum has been the industry's standard dummy text ever since the 1500s, when an unknown printer took a galley of type and scrambled it to make a type specimen book.</p>
    <span class="quote-mark" style="left:184px;top:230px">”</span>
    <div class="portrait" role="img" aria-label="Happy patient sitting in a sunny meadow"></div>
  </aside>

  <div class="abs special">
    <div class="special-photo" role="img" aria-label="Patient in the dental chair during a checkup"></div>
    <h4>New Patient Special!</h4>
    <p>We offer an Initial Patient Examination, X-rays and Cleaning for $79.00.</p>
    <small>Offers are cash patients only.<br>Insurance will be billed at full value.</small>
  </div>

  <h2 class="abs welcome section-title">Welcome</h2>
  <div class="abs lead">Nolan Pravett, DDS, Providing Cosmetic Dentistry Excellence to Patients in Santa Rosa, Sonoma County and the San Francisco Bay Area.</div>
  <div class="abs intro">
    <p>In Santa Rosa, when you're a patient of Dr. Pravett, you can be confident that you're receiving care from the most experienced, knowledgeable, and skilled cosmetic dentist in Sonoma County.</p>
    <p><b>Dr. Pravett is an award-winning leader</b> in restorative dentistry and a genial professional. His humor, dedication, and talent ensure you a pleasant experience and superb, long-lasting results.</p>
  </div>
  <div class="abs motto">"We provide high quality, state-of-the-art, dental care in a comfortable, caring environment."</div>
  <div class="abs office-photo"><div role="img" aria-label="Exterior of the dental office among garden plants"></div></div>

  <h2 class="abs providers section-title">Dr. Pravett Provides</h2>
  <ul class="abs services">
    <li><svg width="11" height="11"><rect width="11" height="11" rx="2" fill="#f3dccd"/><path d="M3 3l4 2.5L3 8z" fill="var(--orange)"/></svg><b>General dentistry</b> - oral hygiene, cavity detection and repair, crowns.</li>
    <li><svg width="11" height="11"><rect width="11" height="11" rx="2" fill="#f3dccd"/><path d="M3 3l4 2.5L3 8z" fill="var(--orange)"/></svg><b>Cosmetic/restorative dentistry</b> - broken or misshapen teeth, crooked smiles, unsightly gaps</li>
    <li><svg width="11" height="11"><rect width="11" height="11" rx="2" fill="#f3dccd"/><path d="M3 3l4 2.5L3 8z" fill="var(--orange)"/></svg><b>Non-metal fillings</b> - nontoxic, durable tooth-colored resin fillings that are proven to provide better results</li>
    <li><svg width="11" height="11"><rect width="11" height="11" rx="2" fill="#f3dccd"/><path d="M3 3l4 2.5L3 8z" fill="var(--orange)"/></svg><b>Tooth shaping</b> - extending, shortening or otherwise reshaping teeth for improved esthetics</li>
    <li><svg width="11" height="11"><rect width="11" height="11" rx="2" fill="#f3dccd"/><path d="M3 3l4 2.5L3 8z" fill="var(--orange)"/></svg><b>Complete smile make-over's</b> - resin veneers that reshape the whole mouth while preserving natural teeth</li>
    <li><svg width="11" height="11"><rect width="11" height="11" rx="2" fill="#f3dccd"/><path d="M3 3l4 2.5L3 8z" fill="var(--orange)"/></svg><b>Tooth whitening</b> - at-home bleaching options to make teeth appear years younger</li>
    <li><svg width="11" height="11"><rect width="11" height="11" rx="2" fill="#f3dccd"/><path d="M3 3l4 2.5L3 8z" fill="var(--orange)"/></svg><b>Laser Dentistry, Sleep Dentistry, and Implant Dentistry with the Finest and Latest Equipment and Materials.</b></li>
    <li><svg width="11" height="11"><rect width="11" height="11" rx="2" fill="#f3dccd"/><path d="M3 3l4 2.5L3 8z" fill="var(--orange)"/></svg><b>Dental Implants to replace missing teeth.</b></li>
    <li><svg width="11" height="11"><rect width="11" height="11" rx="2" fill="#f3dccd"/><path d="M3 3l4 2.5L3 8z" fill="var(--orange)"/></svg><b>Sedation Dentistry so you can be relaxed.</b></li>
  </ul>

  <footer class="abs footer">
    <h3>Contact Us</h3>
    <div class="name">Dr Nolan Pravett * Santa Rosa Dentist</div>
    <div class="info">To contact us outside office hours for an emergency,<br><b>please call (707) 555-0187.</b></div>
    <div class="addr">Nolan Pravett, DDS, FAGD 2240 Larkmoor Ave. Ste B<br>Santa Rosa, CA 95405</div>
    <div class="footer-links">Why we are different<span>|</span>Technologies we offer<span>|</span>Meet Dr. Pravett<span>|</span>Our Staff<span>|</span><br>Contact Us<span>|</span>Privacy Policy<span>|</span> Terms of Use</div>
    <div class="copyright">© 2009, Nolan Pravett, DDS. All Rights Reserved. - Privacy Policy - Terms of Use</div>
  </footer>
</div>
</body>
</html>
```